Cannabis Security Company- Sales Flyer

Take the copy and make a sleek design- no cannabis leave or paraphernalia. Add graphic elements to the Product Offering section

```html
<!DOCTYPE html>
<html lang="en">
<head>
<meta charset="utf-8">
<title>Corval Sales Flyer</title>
<link rel="stylesheet" href="https://fonts.googleapis.com/css2?family=Oswald:wght@500;700&family=Open+Sans:wght@400;600;700&display=swap">
<style>
:root{
  --yellow:#e9b80e;
  --black:#0b0b0b;
  --white:#ffffff;
  --paper:#f4f4f4;
  --stage:#55535a;
  --muted:#444;
}
*{box-sizing:border-box;margin:0;padding:0}
html,body{width:1200px;height:1200px;overflow:hidden}
body{background:var(--stage);font-family:"Open Sans",Arial,sans-serif;position:relative}
.flyer{position:absolute;left:152px;top:20px;width:896px;height:1160px;background:linear-gradient(180deg,var(--white),var(--paper));overflow:hidden}
.headline{position:absolute;left:40px;top:44px;font-family:"Oswald",Arial,sans-serif;font-weight:500;line-height:1.1}
.headline .lead{font-size:34px;color:var(--black)}
.headline .accent{font-size:32px;color:var(--yellow);font-weight:700}
.intro{position:absolute;left:0;top:150px;width:560px;height:290px;background:var(--black);color:var(--white);padding:36px 40px 0 44px;font-size:19px;line-height:1.45}
.team-photo{position:absolute;left:560px;top:40px;width:336px;height:400px;background:var(--yellow)}
.team-photo .figures{position:absolute;left:20px;bottom:0;width:300px;height:340px;background:linear-gradient(180deg,#c9dff2,#8fb3d6 55%,#2a2f36);border-radius:120px 120px 0 0}
.rule{position:absolute;left:0;top:452px;width:896px;height:6px;background:var(--black)}
.offers{position:absolute;left:40px;top:478px;width:470px}
.offers h2{font-family:"Oswald",Arial,sans-serif;font-weight:700;color:var(--yellow);font-size:32px;margin-bottom:12px}
.offers ul{list-style:none}
.offers li{position:relative;padding-left:30px;font-size:14.5px;line-height:1.32;margin-bottom:10px;color:var(--black)}
.offers li b{font-weight:700}
.offers li svg{position:absolute;left:0;top:3px}
.offers .sub{list-style:none;margin-top:4px}
.offers .sub li{padding-left:18px;margin-bottom:3px;font-size:13.5px;color:var(--muted)}
.offers .sub li::before{content:"";position:absolute;left:0;top:5px;border-left:9px solid var(--black);border-top:5px solid transparent;border-bottom:5px solid transparent}
.products{position:absolute;left:520px;top:470px;width:356px;height:250px;background:var(--black);border-radius:18px}
.products .tab{position:absolute;left:24px;top:-34px;width:250px;height:64px;background:var(--yellow);border:4px solid var(--white);border-radius:10px;font-family:"Oswald",Arial,sans-serif;font-weight:700;font-size:30px;color:var(--black);display:flex;align-items:center;justify-content:center}
.product{position:absolute;display:flex;align-items:center;gap:10px;color:var(--white);font-size:13.5px;font-weight:600;white-space:nowrap}
.product .icon{width:42px;height:42px;border-radius:50%;background:var(--yellow);display:flex;align-items:center;justify-content:center;flex:none}
.clients{position:absolute;left:520px;top:740px;width:356px}
.clients h2{font-family:"Oswald",Arial,sans-serif;font-weight:700;color:var(--yellow);font-size:28px;margin-bottom:14px}
.client-grid{display:grid;grid-template-columns:repeat(4,1fr);gap:14px 6px}
.client{font-size:11.5px;font-weight:700;color:#333;display:flex;align-items:center;gap:5px;white-space:nowrap}
.client i{width:9px;height:9px;background:var(--yellow);display:inline-block;flex:none}
.cta-band{position:absolute;left:0;top:960px;width:896px;height:200px;background:var(--black);color:var(--white)}
.cta{position:absolute;left:40px;top:60px;font-family:"Oswald",Arial,sans-serif}
.cta .big{display:block;color:var(--yellow);font-weight:700;font-size:62px;line-height:1}
.cta .small{display:block;font-family:"Open Sans",Arial,sans-serif;font-size:26px;margin-top:4px}
.divider{position:absolute;left:380px;top:50px;width:2px;height:130px;background:var(--white)}
.contact{position:absolute;left:404px;top:88px}
.contact .phone{font-family:"Oswald",Arial,sans-serif;font-weight:700;font-size:34px;line-height:1.25;display:flex;align-items:center;gap:10px}
.contact .line{color:var(--yellow);font-size:16px;font-weight:600;display:flex;align-items:center;gap:10px;margin-top:6px}
.brand-name{position:absolute;right:40px;top:16px;font-family:"Oswald",Arial,sans-serif;font-weight:700;font-size:56px;line-height:1.3;color:var(--white);letter-spacing:2px}
</style>
</head>
<body>
<main class="flyer">
  <header class="headline">
    <div class="lead">Let Corval Take Care of your</div>
    <div class="accent">Surveillance and IT Hardware Needs</div>
  </header>

  <section class="intro">
    <p>Due to the regulations put forth by the State of California, there is high cost associated with being in compliance to maintain your license and not receive fines as it pertains to security for your facility. In addition, the data intense programs with the seed-to-sale program can be a hindrance to you doing what you do best- running your business!</p>
  </section>

  <div class="team-photo" role="img" aria-label="Photo of three smiling business professionals with arms crossed">
    <div class="figures"></div>
  </div>

  <div class="rule"></div>

  <section class="offers">
    <h2>What Corval Can Offer</h2>
    <ul>
      <li><svg width="18" height="14" viewBox="0 0 18 14"><path d="M1 7l5 5L17 1" fill="none" stroke="#e9b80e" stroke-width="3"/></svg><b>Experience</b>- we have been in the IT and video surveillance business for over 20 years</li>
      <li><svg width="18" height="14" viewBox="0 0 18 14"><path d="M1 7l5 5L17 1" fill="none" stroke="#e9b80e" stroke-width="3"/></svg><b>Compliance</b>- our attorney helped write Prop 64 and can keep you in compliance with the ever-changing regulations</li>
      <li><svg width="18" height="14" viewBox="0 0 18 14"><path d="M1 7l5 5L17 1" fill="none" stroke="#e9b80e" stroke-width="3"/></svg><b>Cost Savings</b>- Corval can save you 15-30% over the competition</li>
      <li><svg width="18" height="14" viewBox="0 0 18 14"><path d="M1 7l5 5L17 1" fill="none" stroke="#e9b80e" stroke-width="3"/></svg><b>Speed</b>- our solutions can be designed and implemented within days, not months</li>
      <li><svg width="18" height="14" viewBox="0 0 18 14"><path d="M1 7l5 5L17 1" fill="none" stroke="#e9b80e" stroke-width="3"/></svg><b>Customization</b>- our products are architected around the business not the business around the products</li>
      <li><svg width="18" height="14" viewBox="0 0 18 14"><path d="M1 7l5 5L17 1" fill="none" stroke="#e9b80e" stroke-width="3"/></svg><b>Finance options</b>- Corval offers the following options for purchase
        <ul class="sub">
          <li>Outright purchase- own your own equipment and data</li>
          <li>Leasing with a monthly payment- prevent large outlay of cash</li>
          <li>Managed/cloud offering- we send the gear and manage in a secure location</li>
        </ul>
      </li>
    </ul>
  </section>

  <section class="products">
    <div class="tab">Product Offering</div>
    <div class="product" style="left:24px;top:80px">
      <span class="icon"><svg width="24" height="16" viewBox="0 0 24 16"><rect x="0" y="2" width="15" height="12" rx="2" fill="#0b0b0b"/><path d="M16 7l8-5v12l-8-5z" fill="#0b0b0b"/></svg></span>Video Surveillance
    </div>
    <div class="product" style="left:200px;top:50px">
      <span class="icon"><svg width="20" height="22" viewBox="0 0 20 22"><path d="M10 1l8 3v6c0 6-4 9-8 11C6 19 2 16 2 10V4z" fill="#0b0b0b"/><path d="M10 5l4 1.5v4c0 3-2 5-4 6z" fill="#e9b80e"/></svg></span>Data Security
    </div>
    <div class="product" style="left:44px;top:140px">
      <span class="icon"><svg width="20" height="20" viewBox="0 0 20 20"><path d="M1 1h15l3 3v15H1z" fill="#0b0b0b"/><rect x="5" y="2" width="9" height="6" fill="#e9b80e"/><rect x="4" y="12" width="12" height="6" fill="#e9b80e"/></svg></span>Data Storage
    </div>
    <div class="product" style="left:214px;top:110px">
      <span class="icon"><svg width="22" height="22" viewBox="0 0 22 22"><path d="M5 5L17 17M17 5L5 17M5 5h12" stroke="#0b0b0b" stroke-width="2" fill="none"/><circle cx="5" cy="5" r="3.5" fill="#0b0b0b"/><circle cx="17" cy="5" r="3.5" fill="#0b0b0b"/><circle cx="5" cy="17" r="3.5" fill="#0b0b0b"/><circle cx="17" cy="17" r="3.5" fill="#0b0b0b"/></svg></span>Networking
    </div>
    <div class="product" style="left:64px;top:196px">
      <span class="icon"><svg width="24" height="20" viewBox="0 0 24 20"><path d="M2 7a14 14 0 0 1 20 0M5.5 10.5a9 9 0 0 1 13 0M9 14a4 4 0 0 1 6 0" fill="none" stroke="#0b0b0b" stroke-width="2.4" stroke-linecap="round"/><circle cx="12" cy="17" r="2" fill="#0b0b0b"/></svg></span>Wireless Connectivity
    </div>
  </section>

  <section class="clients">
    <h2>Meet a few of Our Clients</h2>
    <div class="client-grid">
      <span class="client"><i></i>Nortera</span>
      <span class="client">Cloudane</span>
      <span class="client">Pixloft</span>
      <span class="client">Fizzmont</span>
      <span class="client">Vantrel</span>
      <span class="client">Chime Media</span>
      <span class="client">Kestrel TV</span>
      <span class="client">Tunebox</span>
      <span class="client">Sportline</span>
      <span class="client">Staynest</span>
      <span class="client">Ridewell</span>
      <span class="client">Prism Net</span>
      <span class="client">Hearth Realty</span>
    </div>
  </section>

  <footer class="cta-band">
    <div class="cta">
      <span class="big">Call us today</span>
      <span class="small">for a free consultation</span>
    </div>
    <div class="divider"></div>
    <div class="contact">
      <div class="phone"><svg width="16" height="26" viewBox="0 0 16 26"><rect x="1" y="1" width="14" height="24" rx="3" fill="none" stroke="#fff" stroke-width="2"/><circle cx="8" cy="21" r="1.5" fill="#fff"/></svg>555-014-7050</div>
      <div class="line"><svg width="16" height="16" viewBox="0 0 16 16"><circle cx="8" cy="8" r="7" fill="none" stroke="#fff" stroke-width="1.5"/><path d="M1 8h14M8 1c3 3 3 11 0 14M8 1c-3 3-3 11 0 14" fill="none" stroke="#fff" stroke-width="1.2"/></svg>www.corvalsupply-demo.com</div>
      <div class="line"><svg width="16" height="12" viewBox="0 0 16 12"><rect x="1" y="1" width="14" height="10" fill="none" stroke="#fff" stroke-width="1.5"/><path d="M1 1l7 6 7-6" fill="none" stroke="#fff" stroke-width="1.5"/></svg>hello@corvalsupply-demo.com</div>
    </div>
    <div class="brand-name">CORVAL</div>
  </footer>
</main>
</body>
</html>
```